23rd Annual Harrowgate Lantern Film Festival Poster

Design an eye catchy, stylish poster for our 23rd film festival. Be different not just a poster with a film reel. Think outside of the box with a design that will attract peoples attention. Colorful (you choose the colors). Make it fun and creative, like the film festival. Show your talents in the design. Be sure it is new and stylish. Dates are August 21 - 29, 2020. Poster size will be 27 inches by 40 inches

Target Market(s)

Upper Middle class - movie lovers

Font styles to use
Sans Serif

Colors
33a6d7

Requirements
Must have
• NO CLIP ART - be original !
Nice to have
• abstract - think outside the box
Should not have
• CLIP ART

```html
<!DOCTYPE html>
<html lang="en">
<head>
<meta charset="utf-8">
<title>23rd Harrowgate Lantern Film Festival Poster</title>
<link rel="stylesheet" href="https://fonts.googleapis.com/css2?family=Inter:wght@700;800&family=Jost:wght@600;700&display=swap">
<style>
  :root {
    --page-bg: #e6e6e1;
    --poster-orange: #f2511f;
    --soft-orange: #f47f48;
    --steel-blue: #7aa3bd;
    --white: #ffffff;
    --ink: #111111;
  }
  html, body {
    margin: 0;
    padding: 0;
    width: 1200px;
    height: 900px;
    overflow: hidden;
    background: var(--page-bg);
  }
  .poster {
    position: absolute;
    left: 300px;
    top: 15px;
    width: 600px;
    height: 870px;
    background: var(--poster-orange);
    overflow: hidden;
  }
  .film-strip {
    position: absolute;
    left: 22px;
    top: 0;
    width: 185px;
    height: 508px;
  }
  .festival-name-mark {
    position: absolute;
    left: 222px;
    top: 31px;
    width: 351px;
    height: 473px;
    display: flex;
    flex-direction: column;
    justify-content: center;
    font-family: "Jost", sans-serif;
    font-weight: 700;
    font-size: 46px;
    line-height: 1.1;
    color: var(--white);
    text-transform: uppercase;
    white-space: nowrap;
  }
  .edition-number {
    position: absolute;
    left: 6px;
    top: 487px;
    margin: 0;
    font-family: "Inter", sans-serif;
    font-weight: 700;
    font-size: 460px;
    line-height: 1;
    letter-spacing: -0.02em;
    color: var(--soft-orange);
  }
  .edition-suffix {
    position: absolute;
    left: 494px;
    top: 510px;
    font-family: "Inter", sans-serif;
    font-weight: 800;
    font-size: 70px;
    line-height: 1;
    letter-spacing: -0.03em;
    color: var(--steel-blue);
  }
  .festival-title {
    position: absolute;
    left: 0;
    width: 600px;
    top: 701px;
    margin: 0;
    text-align: center;
    font-family: "Jost", sans-serif;
    font-weight: 600;
    font-size: 28px;
    line-height: 40px;
    letter-spacing: -0.01em;
    color: var(--white);
    text-transform: uppercase;
    white-space: nowrap;
  }
  .festival-dates {
    position: absolute;
    left: 0;
    width: 600px;
    top: 760px;
    margin: 0;
    text-align: center;
    font-family: "Jost", sans-serif;
    font-weight: 600;
    font-size: 24px;
    line-height: 34px;
    color: var(--ink);
    white-space: nowrap;
  }
</style>
</head>
<body>
  <main class="poster">
    <svg class="film-strip" viewBox="0 0 185 508" role="img" aria-label="Stylised strip of motion picture film running down the left edge">
      <rect width="185" height="508" fill="var(--soft-orange)"/>
    </svg>

    <div class="festival-name-mark">
      <span>Harrowgate</span>
      <span>Lantern</span>
    </div>

    <p class="edition-number">23</p>
    <span class="edition-suffix">rd</span>

    <h1 class="festival-title">Harrowgate Lantern Film Festival</h1>
    <p class="festival-dates">|| august 21 - 29. 2020 ||</p>
  </main>
</body>
</html>
```